GWNHSB - Website Design

We require a WordPress website for an accounting firm.
Please review our concept design found on our development site:
http://tomlakeweb.ca/gwnholt.
The client would like to carry the look and feel of the National Corporate site http://www.gwn.ca as well.
The site must be mobile ready (responsive)
The client will be providing a collection of staff photos for a contact page
Accounting

```html
<!DOCTYPE html>
<html lang="en">
<head>
<meta charset="utf-8">
<title>Holt Warren &amp; Partners — Chartered Professional Accountants</title>
<link href="https://fonts.googleapis.com/css2?family=Open+Sans:wght@400;600;700&display=swap" rel="stylesheet">
<style>
:root{
  --olive:#8c8a46;
  --olive-light:#b7b56a;
  --olive-dark:#7d7b3b;
  --ink:#1f1f1f;
  --body:#444;
  --footer:#2e2e2e;
  --footer-text:#6f6f6f;
  --white:#fff;
}
*{margin:0;padding:0;box-sizing:border-box}
html,body{width:1009px;height:1200px;overflow:hidden;background:var(--white)}
body{position:relative;font-family:"Open Sans",Arial,sans-serif;color:var(--ink)}
.top-rule{position:absolute;left:0;top:0;width:1009px;height:2px;background:var(--olive)}
.brand{position:absolute;left:83px;top:20px;display:flex;align-items:center;gap:10px}
.brand-mark{width:34px;height:34px;background:var(--olive)}
.brand-text{color:var(--olive-dark);font-weight:600;font-size:18px;line-height:1.2}
.brand-text span{display:block;font-size:11px}
.main-nav{position:absolute;top:52px;left:0;font-size:14px}
.main-nav a{position:absolute;color:var(--ink);text-decoration:none;white-space:nowrap}
.main-nav a.active{color:var(--olive)}
.hero{position:absolute;left:0;top:88px;width:1009px;height:430px;background:linear-gradient(120deg,#1d2a55 0%,#3f5fb5 35%,#c9a493 55%,#e8e9ee 75%,#8d93a3 100%)}
.hero-panel{position:absolute;left:83px;top:121px;width:303px;height:225px;background:var(--olive);color:var(--white);padding:18px 16px}
.hero-kicker{font-size:17px}
.hero-title{font-weight:700;font-size:33px;line-height:1.28;margin-top:2px}
.hero-copy{font-size:10.5px;line-height:1.65;margin-top:8px}
.hero-btn{display:inline-block;margin-top:13px;background:#111;color:var(--white);font-size:10.5px;padding:6px 6px;border-radius:3px}
.dots{position:absolute;top:402px;left:473px;display:flex;gap:13px}
.dots i{width:12px;height:12px;border-radius:50%;background:#9aa087;opacity:.8}
.dots i.on{background:var(--olive);opacity:1}
.welcome{position:absolute;top:540px;left:83px;width:843px;text-align:center}
.welcome h1{font-weight:400;font-size:27px}
.welcome p{font-size:10.5px;line-height:1.7;color:var(--body);margin-top:14px}
.btn{display:inline-block;background:linear-gradient(#bcbb72,#8f8d47);color:var(--white);border-radius:3px;text-shadow:0 1px 1px rgba(0,0,0,.3)}
.welcome .btn{position:absolute;left:375px;top:108px;width:94px;height:38px;line-height:38px;font-size:12.5px}
.services-title{position:absolute;left:82px;top:720px;font-size:26px;font-weight:400}
.pager{position:absolute;left:852px;top:726px;display:flex;gap:2px}
.pager span{width:36px;height:35px;background:var(--olive);display:flex;align-items:center;justify-content:center}
.card{position:absolute;top:788px;width:262px}
.card-img{width:262px;height:142px;border:3px solid #fff;box-shadow:0 0 2px rgba(0,0,0,.45)}
.card h2{font-weight:400;font-size:19px;margin-top:20px;padding-left:2px}
.card p{font-size:9.6px;line-height:1.82;color:var(--body);margin-top:8px}
.card .btn{margin-top:21px;width:73px;height:32px;line-height:32px;text-align:center;font-size:10.5px}
.site-footer{position:absolute;left:0;top:1114px;width:1009px;height:86px;background:var(--footer)}
.foot-nav{position:absolute;left:84px;top:30px;font-size:12px;color:var(--footer-text)}
.foot-nav span{margin-right:32px}
.copyright{position:absolute;left:83px;top:50px;font-size:10.5px;color:var(--footer-text)}
.social{position:absolute;left:799px;top:32px;display:flex;gap:10px}
.social i{width:36px;height:36px;border-radius:50%}
</style>
</head>
<body>
<div class="top-rule"></div>
<header>
  <div class="brand">
    <div class="brand-mark"></div>
    <div class="brand-text">HOLT WARREN &amp; PARTNERS<span>CHARTERED PROFESSIONAL ACCOUNTANTS</span></div>
  </div>
  <nav class="main-nav">
    <a class="active" style="left:493px">Home</a>
    <a style="left:570px">Profile</a>
    <a style="left:650px">Client Services</a>
    <a style="left:778px">Resources</a>
    <a style="left:880px">Contact</a>
  </nav>
</header>

<section class="hero" role="img" aria-label="Photo of an accountant in a suit writing on papers beside a calculator">
  <div class="hero-panel">
    <div class="hero-kicker">Range of services</div>
    <div class="hero-title">Individual and Business</div>
    <div class="hero-copy">Our clients benefit from personalized, quality service that is beyond comparison.</div>
    <span class="hero-btn">Read More</span>
  </div>
  <div class="dots"><i></i><i class="on"></i><i></i></div>
</section>

<section class="welcome">
  <h1>Welcome to Tomlake</h1>
  <p>Nemo enim ipsam voluptatem quia voluptas sit aspernatur aut odit aut fugit, sed quia consequuntur magni dolores eos qui ratione voluptatem sequi nesciunt. Neque porro quis-quam est, qui dolorem ipsum quia dolor sit amet, consectetur, adipisci velit...</p>
  <span class="btn">Read More</span>
</section>

<h2 class="services-title">Our Services</h2>
<div class="pager">
  <span><svg width="10" height="12" viewBox="0 0 10 12"><path d="M7 1 2 6l5 5" fill="none" stroke="#fff" stroke-width="1.6"/></svg></span>
  <span><svg width="10" height="12" viewBox="0 0 10 12"><path d="M3 1l5 5-5 5" fill="none" stroke="#fff" stroke-width="1.6"/></svg></span>
</div>

<article class="card" style="left:82px">
  <div class="card-img" role="img" aria-label="Photo of hands using a calculator over paperwork" style="background:linear-gradient(135deg,#2b3556,#c9a898 45%,#cfe0ea 75%,#8aa7bd)"></div>
  <h2>Accounting Services</h2>
  <p>Nemo enim ipsam voluptatem quia voluptas sit aspernatur aut odit aut fugit, sed quia consequuntur magni dolores eos qui ratione voluptatem...</p>
  <span class="btn">Read More</span>
</article>
<article class="card" style="left:374px">
  <div class="card-img" role="img" aria-label="Photo of a hand touching a tablet showing bar charts" style="background:linear-gradient(135deg,#eef2f6,#cfdcec 40%,#e4c4b0 60%,#5e8fd6 85%)"></div>
  <h2>Financial Statements</h2>
  <p>Nemo enim ipsam voluptatem quia voluptas sit aspernatur aut odit aut fugit, sed quia consequuntur magni dolores eos qui ratione voluptatem...</p>
  <span class="btn">Read More</span>
</article>
<article class="card" style="left:662px">
  <div class="card-img" role="img" aria-label="Photo of a laptop and calculator with a hand holding a pen" style="background:linear-gradient(135deg,#d9dade,#7a7d85 40%,#e9e9ec 65%,#b8a195)"></div>
  <h2>Audit Services</h2>
  <p>Nemo enim ipsam voluptatem quia voluptas sit aspernatur aut odit aut fugit, sed quia consequuntur magni dolores eos qui ratione voluptatem...</p>
  <span class="btn">Read More</span>
</article>

<footer class="site-footer">
  <div class="foot-nav"><span>Home</span><span>Profile</span><span>Client Services</span><span>Resources</span><span>Contact</span></div>
  <div class="copyright">© 2015 tomlakeweb.ca/gwnholt. All Rights Reserved</div>
  <div class="social">
    <i style="background:#2f54a8"></i>
    <i style="background:#3aa6dd"></i>
    <i style="background:#e8941d"></i>
  </div>
</footer>
</body>
</html>
```